High-risk maternity posters

Create a poster (11 x 17) with space for a tear off card (also part of the design). Use text from attached and leave space for two logos similar to those on the original poster. You may modify text.

This poster hangs in physician offices to inform expectant moms about the additional level of care offered for high-risk pregnancies.

Physician

• warm, friendly vibe -

```html
<!DOCTYPE html>
<html lang="en">
<head>
<meta charset="utf-8">
<title>High-Risk Maternity Care Poster</title>
<link rel="stylesheet" href="https://fonts.googleapis.com/css2?family=Source+Sans+3:wght@400;600;700&display=swap">
<style>
  :root {
    --ink: #3c4c66;
    --ink-soft: #5d6c84;
    --navy: #2a3f6e;
    --band-top: #eef2f5;
    --band-bottom: #c9d4de;
    --paper: #ffffff;
    --rule: #9aa7b6;
    --photo-warm: #e9c9b8;
    --photo-light: #f6ece6;
    --photo-shadow: #c79a86;
    --hands-warm: #dcae96;
  }
  * { box-sizing: border-box; margin: 0; padding: 0; }
  html, body { width: 776px; height: 1200px; overflow: hidden; background: var(--paper); }
  body { font-family: "Source Sans 3", sans-serif; color: var(--ink); }

  .poster { position: relative; width: 776px; height: 1200px; overflow: hidden;
    background: linear-gradient(180deg, var(--band-top) 52%, var(--band-bottom) 76%); }

  .hero-photo { position: absolute; left: 0; top: 0; width: 776px; height: 700px; }

  .partner-logos { position: absolute; left: 28px; top: 672px; display: flex; flex-direction: column; gap: 6px; }
  .partner-logo { display: flex; align-items: center; gap: 6px; font-size: 13px; font-weight: 700;
    color: var(--navy); letter-spacing: 0.3px; text-transform: uppercase; line-height: 1; }
  .partner-logo.secondary { font-size: 11px; text-transform: none; }
  .partner-logo .mark { width: 11px; height: 11px; background: var(--navy); }

  .headline { position: absolute; left: 28px; top: 752px; width: 730px; font-size: 22.5px;
    line-height: 27px; color: var(--ink); font-weight: 400; }

  .tear-strip { position: absolute; left: 0; top: 902px; width: 776px; height: 298px;
    background: var(--paper); border-top: 2px dashed var(--rule); display: flex; }
  .tear-strip::before { content: ""; position: absolute; left: 0; right: 0; top: 6px; height: 10px;
    background: var(--band-top); }

  .tab { position: relative; flex: 1; border-right: 1px dashed var(--rule); overflow: hidden; }
  .tab:last-child { border-right: none; }
  .tab-inner { position: absolute; left: 50%; top: 50%; width: 272px; height: 108px;
    transform: translate(-50%, -50%) rotate(-90deg); display: flex; align-items: stretch; padding: 6px 0; }

  .tab-photo { width: 96px; height: 100%; border-radius: 2px;
    background: radial-gradient(circle at 60% 50%, var(--photo-light) 0%, var(--hands-warm) 55%, var(--photo-shadow) 100%); }
  .tab-body { flex: 1; padding: 2px 8px; display: flex; flex-direction: column; justify-content: space-between; }
  .tab-brand { display: flex; align-items: center; gap: 4px; font-size: 11px; font-weight: 700;
    color: var(--navy); text-transform: uppercase; letter-spacing: 0.4px; }
  .tab-brand .mark { width: 8px; height: 8px; background: var(--navy); }
  .tab-copy { font-size: 7.5px; line-height: 9.5px; color: var(--ink-soft); }
  .tab-url { font-size: 7.5px; font-weight: 700; color: var(--ink); line-height: 10px; }
  .tab-partner { font-size: 9px; font-weight: 600; color: var(--navy); }
</style>
</head>
<body>
<main class="poster">

  <svg class="hero-photo" viewBox="0 0 776 700" role="img" aria-label="Photograph of a sleeping newborn wrapped in a pink and white blanket, a parent's hand resting by the baby">
    <defs>
      <radialGradient id="heroTone" cx="0.55" cy="0.35" r="0.8">
        <stop offset="0" stop-color="var(--photo-light)"/>
        <stop offset="0.45" stop-color="var(--photo-warm)"/>
        <stop offset="1" stop-color="var(--photo-shadow)"/>
      </radialGradient>
      <linearGradient id="swoosh" x1="0" y1="0" x2="1" y2="0">
        <stop offset="0" stop-color="#ffffff" stop-opacity="0.9"/>
        <stop offset="1" stop-color="#ffffff" stop-opacity="0.4"/>
      </linearGradient>
    </defs>
    <path d="M0 0 H776 V690 C560 610 280 580 0 610 Z" fill="url(#heroTone)"/>
    <path d="M0 610 C280 580 560 610 776 690 L776 700 C560 624 280 594 0 624 Z" fill="url(#swoosh)"/>
  </svg>

  <div class="partner-logos">
    <div class="partner-logo"><span class="mark"></span>Pedicare Medical Group</div>
    <div class="partner-logo secondary"><span class="mark"></span>Saint Brendan's Health System</div>
  </div>

  <p class="headline">Maternis Medical Group<br>of Kansas and Missouri proudly partners with<br>Saint Brendan's Health System to provide care to expectant<br>mothers with complicated pregnancies and their fetuses.</p>

  <section class="tear-strip" aria-label="Tear-off cards">
    <div class="tab"><div class="tab-inner">
      <div class="tab-photo" role="img" aria-label="Photograph of a newborn's hand held in an adult's hands"></div>
      <div class="tab-body">
        <div class="tab-brand"><span class="mark"></span>Maternis</div>
        <p class="tab-copy">To learn more about high-risk pregnancies and our specialists, visit us online:</p>
        <p class="tab-url">www.maternis.com/kansascity<br>www.saintbrendanshealth.org</p>
        <div class="tab-partner">Saint Brendan's Health System</div>
      </div>
    </div></div>
    <div class="tab"><div class="tab-inner">
      <div class="tab-photo" role="img" aria-label="Photograph of a newborn's hand held in an adult's hands"></div>
      <div class="tab-body">
        <div class="tab-brand"><span class="mark"></span>Maternis</div>
        <p class="tab-copy">To learn more about high-risk pregnancies and our specialists, visit us online:</p>
        <p class="tab-url">www.maternis.com/kansascity<br>www.saintbrendanshealth.org</p>
        <div class="tab-partner">Saint Brendan's Health System</div>
      </div>
    </div></div>
    <div class="tab"><div class="tab-inner">
      <div class="tab-photo" role="img" aria-label="Photograph of a newborn's hand held in an adult's hands"></div>
      <div class="tab-body">
        <div class="tab-brand"><span class="mark"></span>Maternis</div>
        <p class="tab-copy">To learn more about high-risk pregnancies and our specialists, visit us online:</p>
        <p class="tab-url">www.maternis.com/kansascity<br>www.saintbrendanshealth.org</p>
        <div class="tab-partner">Saint Brendan's Health System</div>
      </div>
    </div></div>
    <div class="tab"><div class="tab-inner">
      <div class="tab-photo" role="img" aria-label="Photograph of a newborn's hand held in an adult's hands"></div>
      <div class="tab-body">
        <div class="tab-brand"><span class="mark"></span>Maternis</div>
        <p class="tab-copy">To learn more about high-risk pregnancies and our specialists, visit us online:</p>
        <p class="tab-url">www.maternis.com/kansascity<br>www.saintbrendanshealth.org</p>
        <div class="tab-partner">Saint Brendan's Health System</div>
      </div>
    </div></div>
    <div class="tab"><div class="tab-inner">
      <div class="tab-photo" role="img" aria-label="Photograph of a newborn's hand held in an adult's hands"></div>
      <div class="tab-body">
        <div class="tab-brand"><span class="mark"></span>Maternis</div>
        <p class="tab-copy">To learn more about high-risk pregnancies and our specialists, visit us online:</p>
        <p class="tab-url">www.maternis.com/kansascity<br>www.saintbrendanshealth.org</p>
        <div class="tab-partner">Saint Brendan's Health System</div>
      </div>
    </div></div>
    <div class="tab"><div class="tab-inner">
      <div class="tab-photo" role="img" aria-label="Photograph of a newborn's hand held in an adult's hands"></div>
      <div class="tab-body">
        <div class="tab-brand"><span class="mark"></span>Maternis</div>
        <p class="tab-copy">To learn more about high-risk pregnancies and our specialists, visit us online:</p>
        <p class="tab-url">www.maternis.com/kansascity<br>www.saintbrendanshealth.org</p>
        <div class="tab-partner">Saint Brendan's Health System</div>
      </div>
    </div></div>
    <div class="tab"><div class="tab-inner">
      <div class="tab-photo" role="img" aria-label="Photograph of a newborn's hand held in an adult's hands"></div>
      <div class="tab-body">
        <div class="tab-brand"><span class="mark"></span>Maternis</div>
        <p class="tab-copy">To learn more about high-risk pregnancies and our specialists, visit us online:</p>
        <p class="tab-url">www.maternis.com/kansascity<br>www.saintbrendanshealth.org</p>
        <div class="tab-partner">Saint Brendan's Health System</div>
      </div>
    </div></div>
  </section>

</main>
</body>
</html>
```